Verdana Glen Website

I need a design of homepage for a health and wellness center. We considers self to be young and fresh and want something along that design. We want a main picture/logo/design (or all three), and underneath that 4 pictures to depict what services we do. The four services are Orthopedic Rehab, Neurological Rehab, Speech Pathology and Float. I have attached our logo, and some pictures that might be helpful, but the pictures don't have to be included. Here is an example of what I would like it look. http://pixelquarry.com/web-design/contests/brimlotts-website-design-needed-more-work-come-submit-517306/entries/84162975

Health

```html
<!DOCTYPE html>
<html lang="en">
<head>
<meta charset="utf-8">
<title>Verdana Glen Center for Health + Wellness</title>
<link href="https://fonts.googleapis.com/css2?family=Open+Sans:wght@400;600;700&family=Arimo:wght@400;700&display=swap" rel="stylesheet">
<style>
:root{
  --teal:#5fb3a0;
  --teal-light:#d9efec;
  --green:#8cbf1f;
  --green-dark:#6a9a0c;
  --text:#555;
  --dark:#222;
  --grey:#999;
  --line:#e4e4e4;
}
*{margin:0;padding:0;box-sizing:border-box}
html,body{width:1120px;height:1200px;overflow:hidden;background:#fff}
body{position:relative;font-family:"Arimo",Arial,sans-serif;color:var(--text)}
.abs{position:absolute}
.top-bar{left:0;top:0;width:1120px;height:4px;background:var(--teal)}
.brand{left:92px;top:28px;display:flex;align-items:center;gap:10px}
.brand-dot{width:46px;height:46px;border-radius:50%;background:var(--teal)}
.brand-name{font-family:"Open Sans",sans-serif;font-weight:400;font-size:36px;color:var(--teal);letter-spacing:-1px;line-height:1}
.brand-tag{left:204px;top:68px;font-family:"Open Sans",sans-serif;font-weight:600;font-size:11px;color:var(--green)}
.contact{right:48px;top:20px;font-size:9px;color:var(--grey);display:flex;gap:18px}
.contact b{color:#888;font-weight:700}
.nav{right:48px;top:74px;display:flex;gap:43px;font-size:12px;color:var(--teal)}
.hero{left:0;top:102px;width:1120px;height:334px;background:linear-gradient(90deg,#e2f3f1 0%,#d3ecea 45%,#cfe8e5 100%)}
.hero-photo{position:absolute;left:470px;top:0;width:620px;height:334px;background:radial-gradient(ellipse at 60% 50%,#f3e9d8 0%,#e8e2d6 30%,rgba(210,234,231,0) 70%)}
.hero-title{left:133px;top:62px;width:307px;text-align:center;font-family:"Open Sans",sans-serif;font-weight:600;font-size:30px;line-height:36px;color:var(--teal);padding-bottom:8px;border-bottom:1px solid #fff}
.hero-sub{left:133px;top:158px;width:307px;text-align:center;font-size:20px;color:#888}
.btn{display:flex;align-items:center;justify-content:center;width:171px;height:36px;border-radius:2px;background:linear-gradient(#a4cf2c,#7eb312);border-bottom:2px solid var(--green-dark);color:#fff;font-family:"Open Sans",sans-serif;font-weight:600;font-size:15px;box-shadow:0 8px 10px -8px rgba(0,0,0,.35)}
.hero .btn{position:absolute;left:186px;top:208px}
.dots{left:543px;top:417px;display:flex;gap:5px}
.dots span{width:8px;height:8px;border-radius:50%;background:#fff}
.dots span.on{background:var(--teal)}
.about-title{left:0;top:468px;width:1112px;text-align:center;font-size:19px;color:var(--dark)}
.about-title b{font-weight:700}
.about-text{left:210px;top:502px;width:692px;text-align:center;font-size:11px;line-height:18.4px}
.card{top:602px;width:226px}
.card-img{width:226px;height:150px}
.card h3{margin-top:14px;text-align:center;font-size:19px;font-weight:400;color:var(--dark)}
.card h3 b{font-weight:700}
.card p{margin:12px 10px 0;font-size:11.3px;line-height:18.4px;text-align:justify}
.card .btn{margin:22px 0 0 24px}
.person-photo{width:110px;height:110px;border-radius:50%;border:2px solid #e9dcc6}
.person-name{font-size:16px;font-weight:700;color:var(--teal)}
.person-cred{font-size:14px;font-weight:700;color:#aaa}
.person-bio{width:462px;font-size:11.3px;line-height:18.4px}
.person-bio a{color:var(--teal);font-style:italic;text-decoration:none}
.divider{left:64px;top:1160px;width:560px;border-top:1px dashed #9fd0c5}
.help-photo{left:920px;top:1008px;width:120px;height:192px;border-radius:60px 60px 0 0;background:linear-gradient(#e6d8cc,#f6f1ec)}
.help-title{left:703px;top:1060px;font-family:"Open Sans",sans-serif;font-weight:600;font-size:19px;color:var(--dark)}
.help-text{left:705px;top:1090px;width:210px;font-size:11.5px;line-height:16.5px;color:#777}
.field{left:703px;width:223px;height:35px;border:1px solid #ccc;background:#fff;font-size:10px;color:#555;padding:12px 11px}
</style>
</head>
<body>
<div class="abs top-bar"></div>

<header>
  <div class="abs brand"><span class="brand-dot"></span><span class="brand-name">Verdana Glen</span></div>
  <div class="abs brand-tag">feel better. live better. be better.</div>
  <div class="abs contact">
    <span><b>Address:</b> 117 West 52nd Street Suite 4, New York, NY 10019</span>
    <span><b>Phone:</b> 212-555-0148</span>
    <span><b>Fax:</b> 212.555.0149</span>
  </div>
  <nav class="abs nav"><span>About Us</span><span>Health</span><span>Wellnes Services</span><span>Mind-Body Initiative</span><span>Testimonials</span></nav>
</header>

<section class="abs hero">
  <div class="hero-photo" role="img" aria-label="Smiling woman with arms raised against a pale sea and sky"></div>
  <h1 class="abs hero-title">Where Expertise<br>&amp; Quality Care Meet</h1>
  <div class="abs hero-sub">Feel Better. Live Better. Be Better</div>
  <a class="btn">LEARN MORE</a>
</section>
<div class="abs dots"><span></span><span class="on"></span><span></span></div>

<h2 class="abs about-title"><b>About</b> Us</h2>
<p class="abs about-text">We are proud to be New York City's first comprehensive health + wellness center. Our professional philosophy is to provide paramount rehabilitation, medical, and wellness services in a supportive and nurturing environment. We strive to foster optimal health and well-being in order to improve the quality of life for each of our patients.</p>

<article class="abs card" style="left:52px">
  <div class="card-img" role="img" aria-label="Therapist guiding a patient through a resistance band exercise" style="background:linear-gradient(135deg,#e9e4df,#cfc6bd)"></div>
  <h3><b>Orthopedic</b> Rehab</h3>
  <p>Lorem ipsum dolor sit amet, consectetur adipisicing elit, sed do eiusmod tempor incididunt ut labore et dolore magna aliqua.</p>
  <a class="btn">LEARN MORE</a>
</article>
<article class="abs card" style="left:305px">
  <div class="card-img" role="img" aria-label="Doctor holding a tablet with a glowing brain scan" style="background:linear-gradient(135deg,#dceef7,#8fc6e4)"></div>
  <h3><b>Neurological</b> Rehab</h3>
  <p>Lorem ipsum dolor sit amet, consectetur adipisicing elit, sed do eiusmod tempor incididunt ut labore et dolore magna aliqua.</p>
  <a class="btn">LEARN MORE</a>
</article>
<article class="abs card" style="left:555px">
  <div class="card-img" role="img" aria-label="Counsellor taking notes while talking with a young man" style="background:linear-gradient(135deg,#c8d6b0,#9bb0c4)"></div>
  <h3><b>Speech</b> Pathology</h3>
  <p>Lorem ipsum dolor sit amet, consectetur adipisicing elit, sed do eiusmod tempor incididunt ut labore et dolore magna aliqua.</p>
  <a class="btn">LEARN MORE</a>
</article>
<article class="abs card" style="left:806px">
  <div class="card-img" role="img" aria-label="Group of friends cheering in a sunny meadow" style="background:linear-gradient(#f3e7b4,#9fb65a)"></div>
  <h3><b>Float</b> Pathology</h3>
  <p>Lorem ipsum dolor sit amet, consectetur adipisicing elit, sed do eiusmod tempor incididunt ut labore et dolore magna aliqua.</p>
  <a class="btn">LEARN MORE</a>
</article>

<section class="team">
  <div class="abs person-photo" role="img" aria-label="Portrait of a smiling blonde therapist" style="left:58px;top:1026px;background:radial-gradient(#f7e4c7,#e8c98f)"></div>
  <div class="abs person-name" style="left:204px;top:1026px">Elena R. Whitcombe</div>
  <div class="abs person-cred" style="left:204px;top:1046px">MS, MPhil, MSCS, CCC-SLP</div>
  <p class="abs person-bio" style="left:204px;top:1067px">Ms. Whitcombe is the owner of Hudson Neuro Speech-Language Services, P.C., and co-owner of the Verdana Glen Center for Health + Wellness, New York City's first all-inclusive health &amp; wellness center.&nbsp; <a>Learn more...</a></p>
  <div class="abs divider"></div>
  <div class="abs person-photo" role="img" aria-label="Portrait of a male therapist" style="left:70px;top:1182px;background:radial-gradient(#b89a72,#6e5536)"></div>
  <div class="abs person-name" style="left:202px;top:1180px">Daniel P. Harrow</div>
</section>

<section class="help">
  <div class="abs help-photo" role="img" aria-label="Friendly support agent wearing a headset"></div>
  <h2 class="abs help-title">How Can We Help You?</h2>
  <p class="abs help-text">Simply fill out the form below and one of our experts will Contact you.</p>
  <div class="abs field" style="top:1134px">Your Name</div>
  <div class="abs field" style="top:1177px">Your Phone</div>
</section>
</body>
</html>
```